Land Buying Company Needs Letterhead for Direct Mail Marketing to Land Owners

We are looking for a professional letterhead that we will be including in our direct mail marketing. We will be sending this to land owners who may be interested in selling or purchasing land.

The letterhead needs to be editable. Headers and footers would look nice, but we are open. We would want it to include our address, website, phone, and email info. For right now the address to use for design purposes would the following:

Address: 415 Bramwell Avenue #600
Dallas, TX 75219
Website - www.quillridgeacres.example
Email - info@quillridgeacres.example
Phone - 866-402-ACRE

I have attached our logo zip file that we just had done on Pixel Guild. Let me know what questions you have, and thank you.

```html
<!DOCTYPE html>
<html lang="en">
<head>
<meta charset="utf-8">
<title>Quill Ridge Acres — Letterhead</title>
<link rel="stylesheet" href="https://fonts.googleapis.com/css2?family=Montserrat:wght@600&family=Roboto+Condensed:wght@400&display=swap">
<style>
  :root {
    --forest: #3f5f1e;
    --leaf: #8dc63f;
    --mist: #eef5da;
    --paper: #ffffff;
    --backdrop: #d4d5d7;
    --ink: #3f5f1e;
  }
  * { box-sizing: border-box; margin: 0; padding: 0; }
  html, body { width: 1200px; height: 1200px; overflow: hidden; }
  body { background: var(--backdrop); position: relative; }

  .letterhead {
    position: absolute;
    left: 243px; top: 95px;
    width: 714px; height: 1010px;
    background: var(--paper);
  }

  .brand { position: absolute; left: 30px; top: 26px; display: flex; align-items: center; gap: 12px; }
  .brand__dot { width: 60px; height: 60px; border-radius: 50%; background: var(--forest); }
  .brand__name {
    font-family: "Montserrat", sans-serif; font-weight: 600; color: var(--forest);
    line-height: 1; text-transform: uppercase;
  }
  .brand__name .line1 { display: block; font-size: 30px; letter-spacing: 0.5px; }
  .brand__name .line2 { display: block; font-size: 14px; letter-spacing: 5px; margin-top: 6px; }

  .rule { position: absolute; height: 4px; }
  .rule--dark { background: var(--forest); }
  .rule--light { background: var(--leaf); }
  .header-rule-a { left: 344px; top: 31px; width: 183px; }
  .header-rule-b { left: 530px; top: 31px; width: 184px; }
  .footer-rule-a { left: 0; top: 994px; width: 215px; height: 5px; }
  .footer-rule-b { left: 221px; top: 994px; width: 216px; height: 5px; }

  .watermark {
    position: absolute; left: 207px; top: 355px;
    width: 298px; height: 298px; border-radius: 50%;
    background: var(--mist);
  }

  .contact { position: absolute; left: 196px; top: 902px; list-style: none; }
  .contact li {
    display: flex; align-items: center; height: 21.7px;
    font-family: "Roboto Condensed", sans-serif; font-size: 13px; color: var(--ink);
  }
  .contact svg { width: 15px; height: 15px; fill: var(--leaf); margin-right: 4px; flex: none; }
  .contact .sep { color: var(--ink); margin-right: 1px; }
</style>
</head>
<body>
  <main class="letterhead">
    <header>
      <div class="brand">
        <span class="brand__dot"></span>
        <span class="brand__name"><span class="line1">Quill Ridge</span><span class="line2">Acres</span></span>
      </div>
      <span class="rule rule--dark header-rule-a"></span>
      <span class="rule rule--light header-rule-b"></span>
    </header>

    <div class="watermark"></div>

    <footer>
      <ul class="contact">
        <li>
          <svg viewBox="0 0 24 24"><path d="M6.6 10.8a15.1 15.1 0 0 0 6.6 6.6l2.2-2.2c.3-.3.7-.4 1-.2 1.1.4 2.3.6 3.6.6.6 0 1 .4 1 1V20c0 .6-.4 1-1 1A17 17 0 0 1 3 4c0-.6.4-1 1-1h3.5c.6 0 1 .4 1 1 0 1.3.2 2.5.6 3.6.1.3 0 .7-.2 1z"/></svg>
          <span class="sep">|</span>866-402-ACRE
        </li>
        <li>
          <svg viewBox="0 0 24 24"><path d="M2 5h20v14H2z M3.5 6.5 12 13l8.5-6.5" stroke="#fff" stroke-width="1.5"/></svg>
          <span class="sep">|</span>info@quillridgeacres.example
        </li>
        <li>
          <svg viewBox="0 0 24 24"><circle cx="12" cy="12" r="10"/><path d="M2 12h20M12 2c3 3 3 17 0 20M12 2c-3 3-3 17 0 20M4 7h16M4 17h16" stroke="#fff" stroke-width="1.3" fill="none"/></svg>
          <span class="sep">|</span>www.quillridgeacres.example
        </li>
        <li>
          <svg viewBox="0 0 24 24"><path d="M12 2a7 7 0 0 0-7 7c0 5 7 13 7 13s7-8 7-13a7 7 0 0 0-7-7zm0 9.5A2.5 2.5 0 1 1 12 6.5a2.5 2.5 0 0 1 0 5z"/></svg>
          <span class="sep">|</span>415 Bramwell Avenue #600, Dallas, TX 75219
        </li>
      </ul>
      <span class="rule rule--dark footer-rule-a"></span>
      <span class="rule rule--light footer-rule-b"></span>
    </footer>
  </main>
</body>
</html>
```